Create a wine label for our soon to be released Sparkling Wine

As we are about to release our new Sparkling Wine we are in need of a new label. Dimensions and text as per attached file, the design is more or less free style, but keep it a classic sparkling wine label. Keep it clean. Bottle will be near to black with black/silver cap You can use Script Font. No green, red or gold colours. We like black and silver, but don't be afraid to use some color somewhere (we can always change that). We thought of printing our logo in silver foil so a black label would be nice.

Target Market(s)

wine industry

Font styles to use
Script
Other font styles liked:
• GaramITC

Requirements
Must have
• Dimensions and text as per attached file
Nice to have
• Classic wine label
Should not have
• No gold or red or green colour

```html
<!DOCTYPE html>
<html lang="en">
<head>
<meta charset="utf-8">
<title>Frost Creek – Blanc de Noir Label</title>
<link rel="stylesheet" href="https://fonts.googleapis.com/css2?family=Cinzel:wght@400;600&family=Pinyon+Script&display=swap">
<style>
  :root {
    --backdrop-light: #a8a29f;
    --backdrop-dark: #6f6966;
    --label-black: #131313;
    --label-stripe: #1d1d1d;
    --trim-silver: #c9cdd2;
    --trim-silver-dark: #8d9298;
    --title-silver: #e6e6e6;
    --script-grey: #9a9a9a;
    --detail-grey: #b3b3b3;
    --accent-ice: #8fc9e8;
    --emblem-blue: #3a9fd0;
    --emblem-teal: #7cc1a6;
  }
  * { box-sizing: border-box; margin: 0; padding: 0; }
  html, body { width: 1200px; height: 800px; overflow: hidden; }
  body {
    background: radial-gradient(ellipse at 50% 40%, var(--backdrop-light), var(--backdrop-dark));
    display: flex; align-items: center; justify-content: center;
  }
  .wine-label {
    position: relative;
    width: 540px; height: 700px;
    background:
      repeating-linear-gradient(90deg, var(--label-black) 0 5px, var(--label-stripe) 5px 7px);
    border: 3px solid var(--trim-silver-dark);
    border-radius: 6px;
    box-shadow: 0 10px 30px rgba(0,0,0,.35);
    display: flex; flex-direction: column; align-items: center;
    padding: 70px 40px 0;
  }
  .wine-label::before {
    content: ""; position: absolute; inset: 8px;
    border-top: 4px solid var(--trim-silver);
    border-bottom: 4px solid var(--trim-silver);
    border-left: 1px solid var(--trim-silver);
    border-right: 1px solid var(--trim-silver);
    border-radius: 4px;
    pointer-events: none;
  }
  .brand-name {
    font-family: "Cinzel", serif; font-weight: 400;
    font-size: 54px; letter-spacing: 1px;
    color: var(--title-silver);
    white-space: nowrap;
  }
  .region {
    font-family: "Pinyon Script", cursive;
    font-size: 44px; color: var(--script-grey);
    margin-top: 4px;
  }
  .brand-art {
    width: 170px; height: 160px; margin-top: 36px;
    background: linear-gradient(180deg, var(--emblem-blue) 0 50%, var(--emblem-teal) 100%);
    border-radius: 4px;
  }
  .wine-style {
    font-family: "Cinzel", serif; font-weight: 600;
    font-size: 34px; color: var(--accent-ice);
    margin-top: 64px; letter-spacing: 1px;
    white-space: nowrap;
  }
  .details {
    display: grid; grid-template-columns: auto auto;
    column-gap: 18px; row-gap: 4px;
    margin-top: 14px;
    font-family: "Cinzel", serif; font-size: 17px;
    color: var(--detail-grey);
    white-space: nowrap;
  }
  .details .left { text-align: right; }
</style>
</head>
<body>
  <section class="wine-label">
    <h1 class="brand-name">Frost Creek</h1>
    <p class="region">Tasmania</p>
    <div class="brand-art" role="img" aria-label="Illustration of a bare white tree beside a winding river under blue sky"></div>
    <h2 class="wine-style">Blanc de Noir</h2>
    <div class="details">
      <span class="left">Product of Australia</span><span>2013</span>
      <span class="left">750ml</span><span>Vintage Sparkling</span>
      <span class="left">Alc/Vol 12.5%</span><span>Méthode Traditionnelle</span>
    </div>
  </section>
</body>
</html>
```